Business Card Design for New Game Studio

We need a business card design. We are a new company developing innovative mobile and platform games.

I would like to see very innovative design thats brings out the company's goal and direction.

My Company's goal and direction is to "Evolve the way of gaming, Bring fun and entertainment to all gamers"

Please do use our company logo which I have attached to be included in the design.

Please put in details for name, title, contacts etc ... be creative !!!

Reason: Company logo redesign. Awaiting it. Thanks

Hi all Please do wait for my updated company logo. Thanks

Reason: Still waiting on new company logo. Thanks all

Hi All Designers .... Sorry for the long wait... Please see the new file for my new company logo uploaded. Waiting to see all your creative design. Cheers

Hi All .... Please do not just mass send a whole bunch of similar designs .... Would like to see quality instead of quantity Cheers

Entertainment

```html
<!DOCTYPE html>
<html lang="en">
<head>
<meta charset="utf-8">
<title>Nova Keep – Business Card</title>
<link rel="stylesheet" href="https://fonts.googleapis.com/css2?family=Roboto+Condensed:wght@400;700&display=swap">
<style>
  :root {
    --bg: #e4e4e4;
    --card: #ffffff;
    --ink: #222222;
    --ink-soft: #3a3a3a;
    --teal: #2c4b57;
    --green: #8cc63f;
    --edge: #1d1d1d;
  }
  * { margin: 0; padding: 0; box-sizing: border-box; }
  html, body {
    width: 1200px; height: 900px; overflow: hidden;
    background: var(--bg);
    font-family: "Roboto Condensed", "Arial Narrow", sans-serif;
    color: var(--ink);
  }
  .canvas {
    position: relative; width: 1200px; height: 900px;
  }
  .card {
    position: absolute; left: 280px;
    width: 640px; height: 366px;
    background: var(--card);
    box-shadow: 0 6px 18px rgba(0,0,0,.18);
    overflow: hidden;
  }
  .card--front { top: 70px; }
  .card--back { top: 470px; }

  .brand {
    display: flex; align-items: center; gap: 14px;
  }
  .brand__dot {
    width: 34px; height: 34px; border-radius: 50%;
    background: var(--green);
  }
  .brand__name {
    font-weight: 700; font-size: 40px; letter-spacing: 1px;
    color: var(--ink); text-transform: uppercase; line-height: 1;
  }
  .card--front .brand {
    position: absolute; left: 0; right: 0; top: 0; bottom: 0;
    justify-content: center;
  }
  .card--back .brand {
    position: absolute; left: 40px; top: 160px;
  }
  .card--back .brand__name { font-size: 30px; }
  .card--back .brand__dot { width: 26px; height: 26px; }

  .contact {
    position: absolute; left: 368px; top: 48px; width: 260px;
  }
  .contact__name {
    font-weight: 700; font-size: 22px; color: var(--teal);
    text-transform: uppercase; line-height: 1;
  }
  .contact__title {
    font-size: 13px; color: var(--ink-soft); margin-top: 2px;
  }
  .contact__list { list-style: none; margin-top: 22px; }
  .contact__item {
    display: flex; align-items: center; gap: 10px;
    font-size: 14px; color: var(--ink-soft); line-height: 20px;
  }
  .contact__item svg { width: 14px; height: 14px; fill: var(--green); flex: none; }

  .office {
    position: absolute; left: 368px; top: 238px;
  }
  .office__name {
    font-weight: 700; font-size: 17px; color: var(--teal);
    text-transform: uppercase; line-height: 1.1;
  }
  .office__address {
    font-size: 14px; color: var(--ink-soft); line-height: 17px;
  }

  .band {
    position: absolute; right: 0; bottom: 0; height: 52px;
    display: flex;
  }
  .band__teal { width: 170px; background: var(--teal); }
  .band__green { width: 22px; background: var(--green); margin-left: 4px; }
</style>
</head>
<body>
<main class="canvas">
  <section class="card card--front" aria-label="Card front">
    <div class="brand">
      <span class="brand__dot"></span>
      <span class="brand__name">Nova Keep</span>
    </div>
  </section>

  <section class="card card--back" aria-label="Card back">
    <div class="brand">
      <span class="brand__dot"></span>
      <span class="brand__name">Nova Keep</span>
    </div>

    <div class="contact">
      <h1 class="contact__name">Mara Linden</h1>
      <p class="contact__title">Director</p>
      <ul class="contact__list">
        <li class="contact__item">
          <svg viewBox="0 0 16 16" aria-hidden="true"><path d="M3 1l3 3-2 2c1 2 4 5 6 6l2-2 3 3-2 2C7 15 1 9 1 3z"/></svg>
          +12 555 010 200
        </li>
        <li class="contact__item">
          <svg viewBox="0 0 16 16" aria-hidden="true"><path d="M4 0h8a1 1 0 0 1 1 1v14a1 1 0 0 1-1 1H4a1 1 0 0 1-1-1V1a1 1 0 0 1 1-1zm1 2v10h6V2zm3 11a1 1 0 1 0 0 2 1 1 0 0 0 0-2z"/></svg>
          +12 555 010 200
        </li>
        <li class="contact__item">
          <svg viewBox="0 0 16 16" aria-hidden="true"><path d="M0 3h16v10H0zm1 1v1l7 5 7-5V4z"/></svg>
          hello@novakeep.com
        </li>
        <li class="contact__item">
          <svg viewBox="0 0 16 16" aria-hidden="true"><path d="M8 0a8 8 0 1 0 0 16A8 8 0 0 0 8 0zm0 2c1 1 2 3 2 6s-1 5-2 6c-1-1-2-3-2-6s1-5 2-6zM2 8h12v1H2z"/></svg>
          www.novakeep.com
        </li>
      </ul>
    </div>

    <div class="office">
      <h2 class="office__name">Nova Keep</h2>
      <p class="office__address">Unit 1, Harbour Road, 123<br>Singapore</p>
    </div>

    <div class="band" aria-hidden="true">
      <span class="band__teal"></span>
      <span class="band__green"></span>
    </div>
  </section>
</main>
</body>
</html>
```